Tidal Sparks - Main Menu - Re-Design

I want to have a refresh for this app's main menu. There are some different items on the menu depending on the language (English vs. Non-English) and version (Pro vs. Free). I have attached screenshots of the different conditions. This app is a collection of brain training games.

Need designs for light and dark mode. Need designs for both portrait and landscape mode.

Here is a link to the app in Brisk Market.
https://apps.briskmarket.example/store/apps/details?id=tidalworks.tidalsparks

Here is a link to the app in the Orvel App Store.
https://depot.orvel.example/us/app/tidal-sparks-focus-drills/id519274063?ls=1&mt=8

```html
<!DOCTYPE html>
<html lang="en">
<head>
<meta charset="utf-8">
<title>Tidal Sparks – Main Menu</title>
<link rel="stylesheet" href="https://fonts.googleapis.com/css2?family=Poppins:wght@300;400;600&display=swap">
<style>
  :root {
    --bg: #0a0b2c;
    --text: #ffffff;
    --muted: #b9bbc9;
    --accent: #fdc05c;
    --badge-dot: #f2636b;
    --chip: rgba(255, 255, 255, 0.3);
    --purple-a: #7f46f3; --purple-b: #5a2cbf;
    --yellow-a: #ffd21c; --yellow-b: #f6a521;
    --navy-a: #142590; --navy-b: #0b155e;
    --sky-a: #2fb9ea; --sky-b: #1366bb;
    --orange-a: #ff7d1c; --orange-b: #ff4519;
    --sun-a: #ffd11c; --sun-b: #ffb81a;
    --red-a: #f33842; --red-b: #c30a14;
    --blue-a: #72b4e4; --blue-b: #5a9bd6;
    --violet-a: #6b37d2; --violet-b: #4828a4;
    --lilac-a: #cfa8d6; --lilac-b: #a576c6;
    --green-a: #62d22c; --green-b: #379a0f;
    --lime-a: #93cf58; --lime-b: #79bb42;
  }
  * { box-sizing: border-box; margin: 0; padding: 0; }
  html, body { width: 1200px; height: 556px; overflow: hidden; background: var(--bg); }
  body { font-family: "Poppins", sans-serif; color: var(--text); position: relative; }

  .top-bar { position: absolute; inset: 0 0 auto 0; height: 130px; }
  .greeting { position: absolute; left: 0; right: 0; top: 44px; text-align: center; }
  .greeting__hello { font-size: 41px; font-weight: 300; line-height: 1.1; letter-spacing: 0.2px; }
  .greeting__hello strong { font-weight: 600; }
  .greeting__tagline { font-size: 27px; font-weight: 300; color: var(--muted); line-height: 1.2; }

  .trophy { position: absolute; left: 52px; top: 40px; width: 44px; height: 48px; }
  .trophy__count {
    position: absolute; right: 0; top: -2px; width: 20px; height: 20px; border-radius: 50%;
    background: var(--badge-dot); font-size: 12px; font-weight: 600; text-align: center; line-height: 20px;
  }
  .settings { position: absolute; left: 1053px; top: 48px; width: 38px; height: 38px; }
  .info-button {
    position: absolute; left: 1107px; top: 48px; width: 37px; height: 37px; border-radius: 50%;
    background: var(--accent); color: var(--bg); font-weight: 600; font-size: 22px;
    text-align: center; line-height: 37px;
  }

  .tile {
    position: absolute; width: 333px; height: 155px; border-radius: 5px; overflow: hidden;
    color: var(--text); text-decoration: none;
  }
  .tile__art {
    position: absolute; left: 232px; top: -20px; width: 160px; height: 160px; border-radius: 50%;
  }
  .tile__badge {
    position: absolute; left: 20px; top: 18px; height: 32px; padding: 0 16px; border-radius: 16px;
    background: var(--chip); font-size: 16px; line-height: 32px; font-weight: 400;
    display: flex; align-items: center; gap: 5px;
  }
  .tile__badge svg { width: 12px; height: 14px; }
  .tile__title {
    position: absolute; left: 20px; top: 69px; font-size: 27px; font-weight: 600;
    white-space: nowrap; line-height: 1.2;
  }

  .tile--training { left: 53px; top: 156px; background: linear-gradient(180deg, var(--purple-a), var(--purple-b)); }
  .tile--training .tile__art { background: linear-gradient(180deg, var(--yellow-a), var(--yellow-b)); }
  .tile--games { left: 434px; top: 156px; background: linear-gradient(180deg, var(--navy-a), var(--navy-b)); }
  .tile--games .tile__art { background: linear-gradient(180deg, var(--sky-a), var(--sky-b)); }
  .tile--learning { left: 814px; top: 156px; background: linear-gradient(180deg, var(--orange-a), var(--orange-b)); }
  .tile--learning .tile__art { background: linear-gradient(180deg, var(--sun-a), var(--sun-b)); }
  .tile--schedule { left: 53px; top: 345px; background: linear-gradient(180deg, var(--red-a), var(--red-b)); }
  .tile--schedule .tile__art { background: linear-gradient(180deg, var(--blue-a), var(--blue-b)); }
  .tile--scores { left: 434px; top: 345px; background: linear-gradient(180deg, var(--violet-a), var(--violet-b)); }
  .tile--scores .tile__art { background: linear-gradient(135deg, var(--lilac-a), var(--lilac-b)); }
  .tile--about { left: 810px; top: 345px; background: linear-gradient(180deg, var(--green-a), var(--green-b)); }
  .tile--about .tile__art { background: linear-gradient(180deg, var(--lime-a), var(--lime-b)); }
</style>
</head>
<body>
  <header class="top-bar">
    <div class="trophy" aria-label="Achievements">
      <svg viewBox="0 0 44 48" width="44" height="48" fill="var(--accent)">
        <path d="M8 10h26v6c0 8-5 14-13 14S8 24 8 16z"/>
        <path d="M8 13H3v3c0 5 3 8 7 8" fill="none" stroke="var(--accent)" stroke-width="3"/>
        <path d="M34 13h5v3c0 5-3 8-7 8" fill="none" stroke="var(--accent)" stroke-width="3"/>
        <rect x="19" y="29" width="4" height="9"/>
        <rect x="12" y="38" width="18" height="4" rx="1"/>
      </svg>
      <span class="trophy__count">2</span>
    </div>
    <div class="greeting">
      <h1 class="greeting__hello">Hello, <strong>John Doe</strong></h1>
      <p class="greeting__tagline">Train your skills today</p>
    </div>
    <svg class="settings" viewBox="0 0 38 38" aria-label="Settings" fill="none" stroke="var(--accent)" stroke-width="3" stroke-linejoin="round">
      <path d="M16 3h6l1 5 4 2 4-3 4 4-3 4 2 4 5 1v6l-5 1-2 4 3 4-4 4-4-3-4 2-1 5h-6l-1-5-4-2-4 3-4-4 3-4-2-4-5-1v-6l5-1 2-4-3-4 4-4 4 3 4-2z" transform="translate(0.5 0.5) scale(0.97)"/>
      <circle cx="19" cy="19" r="6"/>
    </svg>
    <div class="info-button" aria-label="Information">i</div>
  </header>

  <nav class="menu" aria-label="Main menu">
    <a class="tile tile--training" href="#training">
      <div class="tile__art" role="img" aria-label="Training Center illustration"></div>
      <span class="tile__badge">NEW</span>
      <span class="tile__title">Training Center</span>
    </a>
    <a class="tile tile--games" href="#games">
      <div class="tile__art" role="img" aria-label="Games List illustration"></div>
      <span class="tile__badge">NEW</span>
      <span class="tile__title">Games List</span>
    </a>
    <a class="tile tile--learning" href="#learning">
      <div class="tile__art" role="img" aria-label="Learning illustration"></div>
      <span class="tile__badge">
        <svg viewBox="0 0 12 14" fill="#fff" aria-hidden="true"><path d="M6 0c1 3 5 5 5 8.5A5 5 0 0 1 1 8.5C1 6 3 5 3 3c1.5 1 2 2 2 3 1-1 1.5-3 1-6z"/></svg>
        HOT
      </span>
      <span class="tile__title">Learning</span>
    </a>
    <a class="tile tile--schedule" href="#schedule">
      <div class="tile__art" role="img" aria-label="Schedule illustration"></div>
      <span class="tile__badge">NEW</span>
      <span class="tile__title">Schedule</span>
    </a>
    <a class="tile tile--scores" href="#scores">
      <div class="tile__art" role="img" aria-label="Scores illustration"></div>
      <span class="tile__badge">NEW</span>
      <span class="tile__title">Scores</span>
    </a>
    <a class="tile tile--about" href="#about">
      <div class="tile__art" role="img" aria-label="About illustration"></div>
      <span class="tile__badge">NEW</span>
      <span class="tile__title">About</span>
    </a>
  </nav>
</body>
</html>
```